Graphic Design Project adhesive label

We are a handkerchief wholesaler and require an adhesive sticker to stick on top left side single cello bag 170mm x 170mm. Then to run down the back of back noting our details. Flat and folded inside bag is a floral and or paisley ladies handkerchief.
Sticker approx 30cm wide 90mm long but folded at 45mm. 45mm down the front of bag and 45mm going down back of bag. Changed cm to mm.

Wording for Front sticker:

Marlowe Cloth
handkerchief
by .Tennick.

Back of sticker:

Made from imported English Marlowe cloth
100% cotton traditional hemstitch finish
www.tennick-example.com

Hi - Sorry made a mistake with measurements should be 170 mm not 170cm. Same with sticker mm's.                                     

Reason: Extending deadline as will be away until wednesday 2/5/13

Reason: Have been away and have not had a chance to consider designs, thanks for your patience. T

Target Market(s)

mature generally

Industry/Entity Type

Floral

Requirements
Must have
• prefer a lighter background
Nice to have
• Apart from wording some sort of back ground design, colour or symbol

```html
<!DOCTYPE html>
<html lang="en">
<head>
<meta charset="utf-8">
<title>Marlowe Cloth Handkerchief Label</title>
<link href="https://fonts.googleapis.com/css2?family=Sorts+Mill+Goudy&display=swap" rel="stylesheet">
<style>
  :root {
    --sand: #dcc39d;
    --sand-deep: #cfb38a;
    --cocoa: #5b3418;
    --earth: #6e411e;
    --earth-deep: #62381a;
    --cream: #f6dd9c;
  }
  html, body {
    margin: 0;
    padding: 0;
    width: 1200px;
    height: 3603px;
    overflow: hidden;
    background: #ffffff;
  }
  .label {
    position: relative;
    width: 1200px;
    height: 3603px;
    overflow: hidden;
    font-family: "Sorts Mill Goudy", "Palatino Linotype", Georgia, serif;
  }
  .front-panel {
    position: absolute;
    left: 0; top: 0;
    width: 1200px; height: 1797px;
    background: var(--sand);
  }
  .back-panel {
    position: absolute;
    left: 0; top: 1797px;
    width: 1200px; height: 1806px;
    background: linear-gradient(180deg, var(--earth) 0%, var(--earth-deep) 100%);
  }
  .brand-mark {
    position: absolute;
    left: 0; top: 160px;
    width: 1200px;
    text-align: center;
    color: var(--cocoa);
  }
  .brand-dot {
    display: block;
    width: 200px; height: 200px;
    margin: 0 auto 40px;
    border-radius: 50%;
    background: var(--cocoa);
  }
  .brand-name {
    font-size: 84px;
    line-height: 1;
    letter-spacing: 4px;
  }
  .divider {
    position: absolute;
    left: 373px;
    width: 457px;
    height: 14px;
    background: var(--cocoa);
    opacity: 0.55;
  }
  .divider-top { top: 817px; }
  .divider-bottom { top: 1468px; }
  .front-title {
    position: absolute;
    left: 0; top: 930px;
    width: 1200px;
    margin: 0;
    text-align: center;
    color: var(--cocoa);
    font-weight: 400;
    font-size: 106px;
    line-height: 127px;
    text-transform: uppercase;
  }
  .back-copy {
    position: absolute;
    left: 0; top: 2010px;
    width: 1200px;
    margin: 0;
    text-align: center;
    color: var(--cream);
    font-size: 98px;
    line-height: 181px;
  }
  .web-address {
    position: absolute;
    left: 0; top: 3400px;
    width: 1200px;
    margin: 0;
    text-align: center;
    color: var(--cream);
    font-size: 98px;
    line-height: 1.2;
  }
</style>
</head>
<body>
  <main class="label">
    <section class="front-panel" role="img" aria-label="Light sand background with a faint looping flourish pattern"></section>
    <section class="back-panel" role="img" aria-label="Rich brown background with a subtle diamond lattice pattern"></section>

    <div class="brand-mark">
      <span class="brand-dot"></span>
      <div class="brand-name">Marlowe Cloth</div>
    </div>

    <div class="divider divider-top" role="img" aria-label="Decorative flourish divider"></div>
    <h1 class="front-title">Marlowe Cloth<br>Handkerchief<br>by Tennick.</h1>
    <div class="divider divider-bottom" role="img" aria-label="Decorative flourish divider"></div>

    <p class="back-copy">Made from<br>imported English<br>Marlowe cloth<br>100% cotton<br>traditional<br>hemstitch finish</p>
    <p class="web-address">www.tennick-example.com</p>
  </main>
</body>
</html>
```